Business IT Services Billboard to attract local small businesses

We are Brivolane, a premier Managed Service Provider (MSP) specializing in comprehensive IT services and VOIP phone solutions exclusively for businesses. Our goal is to create a dynamic and visually engaging billboard advertisement that not only highlights our cutting-edge IT solutions but also emphasizes our state-of-the-art VOIP phone services. This billboard should communicate our commitment to providing innovative, reliable, and holistic technology solutions.
Target Market(s)
small business
Industry/Entity Type
Information Technology
Colors
Designer to choose colors to be used in the design.
Look and feel
Each slider illustrates characteristics of the customer's brand and the style your logo design should communicate.

```html
<!DOCTYPE html>
<html lang="en">
<head>
<meta charset="utf-8">
<title>Brivolane – IT and VOIP Services Billboard</title>
<link rel="stylesheet" href="https://fonts.googleapis.com/css2?family=Saira+Condensed:wght@600;700&family=Poppins:wght@500;600;700&display=swap">
<style>
  :root {
    --page-bg: #d4d4d4;
    --board-bg: #ffffff;
    --navy: #0d1b33;
    --brand-blue: #1a6fbf;
    --orange-start: #e25408;
    --orange-end: #ff8a00;
    --rule: #c9c9c9;
    --photo-a: #5f6f82;
    --photo-b: #a9b4c0;
  }
  * { margin: 0; padding: 0; box-sizing: border-box; }
  html, body { width: 1185px; height: 1200px; overflow: hidden; }
  body {
    background: radial-gradient(ellipse at center, #e6e6e6 0%, var(--page-bg) 70%);
    position: relative;
  }
  .billboard {
    position: absolute;
    left: 30px; top: 436px;
    width: 1125px; height: 328px;
    background: var(--board-bg);
    box-shadow: 0 18px 30px rgba(0,0,0,0.22);
    overflow: hidden;
    font-family: "Poppins", sans-serif;
  }
  .brand-name {
    position: absolute;
    left: 40px; top: 74px;
    font-family: "Poppins", sans-serif;
    font-weight: 700;
    font-size: 31px;
    color: var(--brand-blue);
    letter-spacing: -0.5px;
  }
  .brand-divider {
    position: absolute;
    left: 211px; top: 26px;
    width: 1px; height: 134px;
    background: var(--rule);
  }
  .lead-tag {
    position: absolute;
    left: 240px; top: 27px;
    width: 347px; height: 31px;
    background: linear-gradient(90deg, var(--orange-start), var(--orange-end));
    clip-path: polygon(0 0, 97% 0, 100% 100%, 0 100%);
    color: #fff;
    font-family: "Saira Condensed", sans-serif;
    font-weight: 600;
    font-size: 23px;
    line-height: 31px;
    padding-left: 10px;
    letter-spacing: 0.3px;
  }
  .headline {
    position: absolute;
    left: 239px; top: 58px;
    font-family: "Saira Condensed", sans-serif;
    font-weight: 700;
    line-height: 0.98;
    letter-spacing: 0.3px;
  }
  .headline .line-one { display: block; font-size: 55px; color: var(--navy); }
  .headline .line-two { display: block; font-size: 63px; color: var(--brand-blue); }
  .tagline {
    position: absolute;
    left: 46px; top: 174px;
    font-weight: 600;
    font-size: 15.5px;
    color: var(--navy);
  }
  .web-band {
    position: absolute;
    left: 0; top: 214px;
    width: 711px; height: 48px;
    background: linear-gradient(90deg, var(--orange-start), var(--orange-end));
    clip-path: polygon(0 0, 100% 0, 98.4% 100%, 0 100%);
    display: flex; align-items: center;
    padding-left: 46px;
    color: #fff;
  }
  .web-band .lead { font-weight: 600; font-size: 16px; }
  .web-band .pointer { margin: 0 16px 0 20px; width: 0; height: 0;
    border-top: 7px solid transparent; border-bottom: 7px solid transparent; border-left: 9px solid #fff; }
  .web-band .url { font-weight: 600; font-size: 25px; letter-spacing: 0.2px; }
  .call-row {
    position: absolute;
    left: 46px; top: 270px;
    height: 52px;
    display: flex; align-items: center;
    color: var(--navy);
  }
  .call-row .label { font-weight: 600; font-size: 19px; margin-right: 18px; }
  .call-row .phone-icon { width: 40px; height: 40px; margin-right: 8px; }
  .call-row .number { font-weight: 700; font-size: 44px; letter-spacing: -0.5px; }
  .visual { position: absolute; left: 0; top: 0; width: 1125px; height: 328px; }
</style>
</head>
<body>
  <section class="billboard">
    <div class="brand-name">Brivolane</div>
    <div class="brand-divider"></div>

    <div class="lead-tag">ELEVATE YOUR BUSINESS WITH</div>
    <h1 class="headline">
      <span class="line-one">NEXT-GEN IT AND</span>
      <span class="line-two">VOIP SERVICES</span>
    </h1>
    <p class="tagline">Innovative IT and VOIP Solutions Tailored for Your Business Success.</p>

    <div class="web-band">
      <span class="lead">Transform Your Tech Today at</span>
      <span class="pointer"></span>
      <span class="url">www.brivolane.com</span>
    </div>

    <div class="call-row">
      <span class="label">CALL US TODAY</span>
      <svg class="phone-icon" viewBox="0 0 40 40" aria-hidden="true">
        <circle cx="20" cy="20" r="19" fill="#1a6fbf"/>
        <circle cx="20" cy="20" r="14.5" fill="none" stroke="#fff" stroke-width="1.6"/>
        <path d="M14 12.5c1-.8 2-.7 2.6.2l1.6 2.6c.5.8.3 1.6-.4 2.2l-1 .8c.8 2 2.4 3.8 4.6 4.8l.8-1c.6-.7 1.5-.9 2.3-.4l2.6 1.6c.9.6 1 1.7.2 2.6-1.5 1.6-3.3 2.2-5.4 1.2-4.2-2-7.4-5.4-8.8-9.6-.6-2 .1-3.8 1.9-5z" fill="#fff"/>
      </svg>
      <span class="number">(555) 418-2970</span>
    </div>

    <svg class="visual" viewBox="0 0 1125 328" aria-hidden="false">
      <defs>
        <linearGradient id="photo-tone" x1="0" y1="0" x2="1" y2="1">
          <stop offset="0" stop-color="var(--photo-a)"/>
          <stop offset="1" stop-color="var(--photo-b)"/>
        </linearGradient>
      </defs>
      <polygon class="frame-top" points="735,22 998,22 993,40 742,40 706,190 688,190" fill="#1a6fbf"/>
      <polygon class="frame-bottom" points="1068,135 1098,135 1048,300 800,300 806,286 1040,286" fill="#1a6fbf"/>
      <polygon class="photo" role="img" aria-label="Photo of a smiling support agent wearing a headset in a modern office"
        points="742,40 1080,40 1051,286 701,286" fill="url(#photo-tone)"/>
    </svg>
  </section>
</body>
</html>
```